Lumo4Kart - a fintech company - business card

We need a business card design for our Payments Technology company in Sydney, Australia. We provide business with payment solutions expanding across EFTPOS machines, online payment gateways and mobile payment solutions. We would like to see designs that are clean, classy and professional.
Target Market(s)
Business professionals, executives, c-suite
Industry/Entity Type
Fintech
Contact Information for Business Card
Will be on 400gsm. Logo will most likely be spot gloss unless designer recommends otherwise.
Font styles to use
Sans Serif
Requirements
Must have
- We need our website (lumo4kart.com.au), email (contact@lumo4kart.com.au), mobile (0432 587 904) and direct phone number (02 6815 3927) to feature on the card along with our logo (attached) and the words "EFTPOS | ONLINE | MOBILE"
- Font = Roboto

```html
<!DOCTYPE html>
<html lang="en">
<head>
<meta charset="UTF-8">
<title>Lumo4Kart – Business Card</title>
<link rel="stylesheet" href="https://fonts.googleapis.com/css2?family=Roboto:wght@400;500;700&display=swap">
<style>
  :root {
    --brand-blue: #2a659a;
    --brand-grey: #6d6e70;
    --text-grey: #5a5a5a;
    --card-white: #ffffff;
    --page-bg: #ecebe8;
    --card-shadow: 0 6px 18px rgba(0, 0, 0, 0.18);
  }
  * { box-sizing: border-box; margin: 0; padding: 0; }
  html, body {
    width: 1200px;
    height: 920px;
    overflow: hidden;
    background: var(--page-bg);
    font-family: "Roboto", Arial, sans-serif;
  }
  .canvas {
    position: relative;
    width: 1200px;
    height: 920px;
  }
  .card {
    position: absolute;
    top: 314px;
    width: 536px;
    height: 300px;
    box-shadow: var(--card-shadow);
  }

  /* Front */
  .card-front {
    left: 46px;
    background: var(--brand-blue);
    display: flex;
    flex-direction: column;
    align-items: center;
    justify-content: center;
    color: var(--card-white);
  }
  .brand-dot {
    width: 84px;
    height: 84px;
    border-radius: 50%;
    background: var(--card-white);
    margin-bottom: 14px;
  }
  .brand-name {
    font-weight: 700;
    font-size: 41px;
    letter-spacing: 0.5px;
    line-height: 1;
  }
  .tagline {
    margin-top: 8px;
    font-weight: 500;
    font-size: 13px;
    letter-spacing: 2.4px;
  }

  /* Back */
  .card-back {
    left: 628px;
    background: var(--card-white);
    display: flex;
    align-items: center;
  }
  .brand-block {
    width: 290px;
    display: flex;
    flex-direction: column;
    align-items: center;
    padding-left: 10px;
  }
  .card-back .brand-dot {
    background: var(--brand-blue);
    width: 86px;
    height: 86px;
  }
  .card-back .brand-name {
    color: var(--brand-grey);
    font-size: 40px;
  }
  .card-back .tagline {
    color: var(--brand-blue);
  }
  .divider {
    width: 1.5px;
    height: 186px;
    background: var(--brand-blue);
    margin-right: 20px;
  }
  .contact-block {
    color: var(--text-grey);
    font-size: 12.5px;
    line-height: 1.5;
  }
  .person-name {
    color: var(--brand-blue);
    font-weight: 700;
    font-size: 17px;
    letter-spacing: 0.4px;
  }
  .person-role { margin-bottom: 8px; }
  .address { margin-bottom: 8px; }
  .contact-list { list-style: none; }
  .contact-list li {
    display: flex;
    align-items: center;
    gap: 9px;
    height: 19px;
  }
  .contact-list svg {
    width: 11px;
    height: 11px;
    fill: var(--brand-blue);
    flex-shrink: 0;
  }
</style>
</head>
<body>
<main class="canvas">

  <section class="card card-front" aria-label="Business card front">
    <div class="brand-dot"></div>
    <div class="brand-name">LUMO4KART</div>
    <div class="tagline">EFTPOS | ONLINE | MOBILE</div>
  </section>

  <section class="card card-back" aria-label="Business card back">
    <div class="brand-block">
      <div class="brand-dot"></div>
      <div class="brand-name">LUMO4KART</div>
      <div class="tagline">EFTPOS | ONLINE | MOBILE</div>
    </div>
    <div class="divider"></div>
    <div class="contact-block">
      <div class="person-name">DANIEL HARCOURT</div>
      <div class="person-role">Senior Consultant</div>
      <div class="address">417 W 12th St. Ste 208B<br>Fairview, VA 23517</div>
      <ul class="contact-list">
        <li>
          <svg viewBox="0 0 12 12" aria-hidden="true"><path d="M3 0h6a1 1 0 0 1 1 1v10a1 1 0 0 1-1 1H3a1 1 0 0 1-1-1V1a1 1 0 0 1 1-1zm0.6 1.4v7.8h4.8V1.4zM6 9.8a0.7 0.7 0 1 0 0 1.4a0.7 0.7 0 1 0 0-1.4z"/></svg>
          <span>(0432 587 904)</span>
        </li>
        <li>
          <svg viewBox="0 0 12 12" aria-hidden="true"><path d="M2.4 0.5l2 2.3-1.1 1.5c0.7 1.6 2 2.9 3.6 3.7l1.5-1.1 2.3 2-1.4 2.2C4.4 10.8 1 7.4 0.4 2z"/></svg>
          <span>(02 6815 3927)</span>
        </li>
        <li>
          <svg viewBox="0 0 12 12" aria-hidden="true"><path d="M0 2h12v8H0zm1.2 1.2v0.3L6 6.6l4.8-3.1v-0.3zm0 1.7v3.9h9.6V4.9L6 8z"/></svg>
          <span>contact@lumo4kart.com.au</span>
        </li>
        <li>
          <svg viewBox="0 0 12 12" aria-hidden="true"><path d="M6 0a6 6 0 1 0 0 12A6 6 0 1 0 6 0zm0 1.2c0.8 0 1.5 1.8 1.6 4.2H4.4C4.5 3 5.2 1.2 6 1.2zM1.2 6.6h2.1c0.1 1.6 0.4 2.9 0.9 3.7A4.8 4.8 0 0 1 1.2 6.6zm0-1.2a4.8 4.8 0 0 1 3-3.7c-0.5 0.8-0.8 2.1-0.9 3.7zm3.2 1.2h3.2C7.5 9 6.8 10.8 6 10.8S4.5 9 4.4 6.6zm4.3 0h2.1a4.8 4.8 0 0 1-3 3.7c0.5-0.8 0.8-2.1 0.9-3.7zm0-1.2c-0.1-1.6-0.4-2.9-0.9-3.7a4.8 4.8 0 0 1 3 3.7z"/></svg>
          <span>lumo4kart.com.au</span>
        </li>
      </ul>
    </div>
  </section>

</main>
</body>
</html>
```